Website image, "above the fold"

I'm not loving any of the concepts that have been presented. I uploaded an image that perhaps I can use instead. I would like to replace the image of the seed growing with a little pine tree, if possible I would like to have it in similar color to stand out.

I am looking for an image for the "above the fold" area of my website. here is a link to one you did that would be perfect. Can you help me do something similar? https://www.artpitchhub.com/design/58209413

the slogan for my site is: Pave your path to a prosperous future

Under the slogan it would say: Fee-only fiduciary guidance to grow your wealth now and manage it throughout retirement.

Under that there would be a button that would say: BOOK YOUR PROSPERITY STRATEGY SESSION

I like the design idea of the one in the link.

If that does not make sense, let me know.

I really like the one that is in the image in the link provided. I also need a really light sky background, so my company logo will stand out. White is probably preferable. Or white clouds, like the sample link.

My website is maplebrookfinancialpartners.com

Target Market(s)

People who need help with investment and retirement plans

Industry/Entity Type

financial

Requirements
Nice to have
• I would like to see the image updated to have the little pine tree. I would also like to see the background of the image changed to my company color of green for comparison.

```html
<!DOCTYPE html>
<html lang="en">
<head>
<meta charset="utf-8">
<title>Maplebrook Financial Partners – Prosperous Future</title>
<link rel="stylesheet" href="https://fonts.googleapis.com/css2?family=Montserrat:wght@500;700;800&display=swap">
<style>
  :root {
    --bronze: #8e6a3f;
    --forest: #36503f;
    --gold: #b8973f;
    --gold-light: #e2c987;
    --white: #ffffff;
  }
  html, body {
    margin: 0;
    padding: 0;
    width: 1200px;
    height: 733px;
    overflow: hidden;
    background: var(--white);
  }
  .hero {
    position: relative;
    width: 1200px;
    height: 733px;
    background: var(--white);
    font-family: "Montserrat", Arial, sans-serif;
    overflow: hidden;
  }
  .landscape { position: absolute; left: 0; top: 0; }
  .brand {
    position: absolute;
    left: 37px;
    top: 98px;
    display: flex;
    align-items: center;
    gap: 8px;
    font-weight: 700;
    font-size: 16px;
    letter-spacing: 0.3px;
    color: var(--bronze);
    line-height: 1.2;
  }
  .brand-mark {
    width: 12px;
    height: 12px;
    background: var(--forest);
    flex: none;
  }
  .headline {
    position: absolute;
    left: 0;
    top: 65px;
    width: 1200px;
    margin: 0;
    text-align: center;
    font-weight: 800;
    font-size: 47px;
    line-height: 48px;
    color: var(--bronze);
    letter-spacing: 0.3px;
  }
  .headline .accent { color: var(--forest); }
  .rule {
    position: absolute;
    top: 141px;
    height: 3px;
    width: 80px;
    background: var(--bronze);
  }
  .rule-left { left: 201px; clip-path: polygon(0 50%, 100% 0, 100% 100%); }
  .rule-right { left: 916px; clip-path: polygon(0 0, 100% 50%, 0 100%); }
  .pointer { position: absolute; left: 562px; top: 186px; }
  .subhead {
    position: absolute;
    left: 0;
    top: 242px;
    width: 1200px;
    margin: 0;
    text-align: center;
    font-weight: 500;
    font-size: 23px;
    line-height: 30px;
    color: var(--forest);
  }
  .subhead .accent { color: var(--bronze); }
  .cta {
    position: absolute;
    left: 316px;
    top: 593px;
    display: flex;
    align-items: center;
    gap: 12px;
  }
  .cta-pill {
    height: 46px;
    padding: 0 13px;
    border-radius: 23px;
    background: linear-gradient(180deg, var(--gold-light) 0%, var(--gold) 55%, #9c7c2f 100%);
    color: var(--white);
    font-weight: 800;
    font-size: 22px;
    line-height: 46px;
  }
  .cta-label {
    color: var(--white);
    font-weight: 700;
    font-size: 22px;
  }
</style>
</head>
<body>
<main class="hero">
  <svg class="landscape" width="1200" height="733" viewBox="0 0 1200 733" role="img" aria-label="Black and white photograph of a snowy mountain range rising to the right above a dark valley">
    <defs>
      <linearGradient id="rockFade" x1="0" y1="0" x2="0" y2="1">
        <stop offset="0" stop-color="#d8d8d8"/>
        <stop offset="0.45" stop-color="#8a8a8a"/>
        <stop offset="0.78" stop-color="#1a1a1a"/>
        <stop offset="1" stop-color="#050505"/>
      </linearGradient>
    </defs>
    <path fill="url(#rockFade)" stroke="var(--gold)" stroke-width="6" stroke-linejoin="round"
      d="M-4,384 L49,404 L109,380 L179,376 L219,370 L269,392 L319,430 L349,467 L409,478 L449,486 L479,452 L519,454 L594,373 L629,375 L689,430 L729,390 L789,370 L849,345 L909,294 L989,262 L1039,195 L1069,150 L1149,90 L1204,58 L1204,740 L-4,740 Z"/>
  </svg>

  <div class="brand"><span class="brand-mark"></span><span>Maplebrook<br>Financial Partners</span></div>

  <h1 class="headline">PAVE YOUR PATH TO<br>A PROSPEROUS <span class="accent">FUTURE</span></h1>
  <span class="rule rule-left"></span>
  <span class="rule rule-right"></span>

  <svg class="pointer" width="72" height="32" viewBox="0 0 72 32" aria-hidden="true">
    <rect x="0" y="0" width="72" height="4" fill="var(--forest)"/>
    <polygon points="14,4 58,4 36,31" fill="var(--forest)"/>
  </svg>

  <p class="subhead">FEE-ONLY FIDUCIARY GUIDANCE TO<br><span class="accent">GROW YOUR WEALTH</span> NOW AND MANAGE<br>IT THROUGHOUT RETIREMENT.</p>

  <div class="cta">
    <span class="cta-pill">BOOK YOUR</span>
    <span class="cta-label">PROSPERITY STRATEGY SESSION</span>
  </div>
</main>
</body>
</html>
```